Business Card Design Project

I am looking for a business card that includes the logo that I am uploading. It is an Interior Design business. This card must include the following (in addition to the logo):
Lena Vart
Interior Designer - Allied Member, NPDG
4213 Willowmere Lane
Brennock, MN 55099
612-555-0187
lenapvart@orbimail.test
lenavartspaces.test

Industry/Entity Type

Business

Requirements
Must have
• This card must include the following (in addition to the logo):
Lena Vart
4213 Willowmere Lane
Brennock, MN 55099
612-555-0187
lenapvart@orbimail.test
lenavartspaces.test

```html
<!DOCTYPE html>
<html lang="en">
<head>
<meta charset="utf-8">
<title>Lena Vart Interiors – Business Card</title>
<link href="https://fonts.googleapis.com/css2?family=Arimo:wght@400;700&display=swap" rel="stylesheet">
<style>
  :root {
    --page-bg: #f2eded;
    --card-beige: #e6dccf;
    --card-white: #ffffff;
    --brand-brown: #4b3b2d;
    --text-dark: #3e342c;
    --text-soft: #6a5e54;
    --card-shadow: 0 6px 18px rgba(60, 45, 35, 0.18);
  }
  * { box-sizing: border-box; margin: 0; padding: 0; }
  html, body {
    width: 1200px;
    height: 951px;
    overflow: hidden;
    background: var(--page-bg);
    font-family: "Arimo", Arial, sans-serif;
  }
  .canvas { position: relative; width: 1200px; height: 951px; }

  .card {
    position: absolute;
    width: 660px;
    height: 377px;
    box-shadow: var(--card-shadow);
    overflow: hidden;
  }

  /* Front side */
  .card-front { left: 110px; top: 70px; background: var(--card-beige); }
  .card-front .brand-block {
    position: absolute; left: 120px; top: 45px;
    width: 215px; height: 250px; background: var(--brand-brown);
  }
  .card-front .brand-name {
    position: absolute; left: 120px; top: 305px; width: 215px;
    font-size: 23px; color: var(--brand-brown); font-weight: 400;
    letter-spacing: -0.4px; white-space: nowrap;
  }

  /* Back side */
  .card-back { left: 430px; top: 480px; background: var(--card-white); }
  .card-back .info-band {
    position: absolute; left: 0; top: 0; width: 100%; height: 270px;
    background: var(--card-beige);
  }
  .card-back .person-name {
    position: absolute; left: 26px; top: 26px;
    font-size: 24px; color: var(--text-dark); font-weight: 400;
  }
  .card-back .person-title {
    position: absolute; left: 26px; top: 60px;
    font-size: 13px; color: var(--text-soft);
  }
  .card-back .brand-block {
    position: absolute; left: 40px; top: 100px;
    width: 175px; height: 200px; background: var(--brand-brown);
  }
  .card-back .brand-name {
    position: absolute; left: 40px; top: 310px; width: 175px;
    font-size: 19px; color: var(--brand-brown); font-weight: 400;
    letter-spacing: -0.4px; white-space: nowrap;
  }
  .contact-list {
    position: absolute; left: 345px; top: 112px;
    list-style: none; font-size: 17px; color: var(--text-dark); line-height: 1.2;
  }
  .contact-list li { display: flex; align-items: flex-start; gap: 10px; margin-bottom: 8px; }
  .contact-list li.address { margin-bottom: 14px; }
  .contact-list svg { width: 16px; height: 16px; flex: none; margin-top: 2px; fill: var(--text-dark); }
</style>
</head>
<body>
<main class="canvas">

  <section class="card card-front" aria-label="Business card front">
    <div class="brand-block"></div>
    <p class="brand-name">lena vart interiors, llc</p>
  </section>

  <section class="card card-back" aria-label="Business card back">
    <div class="info-band"></div>
    <h1 class="person-name">Lena Vart</h1>
    <p class="person-title">Interior Designer - Allied Member, NPDG</p>
    <div class="brand-block"></div>
    <p class="brand-name">lena vart interiors, llc</p>

    <ul class="contact-list">
      <li class="address">
        <svg viewBox="0 0 16 16" aria-hidden="true"><path d="M8 1 1 7.5h2V15h4v-4.5h2V15h4V7.5h2z"/></svg>
        <span>4213 Willowmere Lane<br>Brennock, MN 55099</span>
      </li>
      <li>
        <svg viewBox="0 0 16 16" aria-hidden="true"><path d="M4 1.5 6.2 4 5 6c.8 1.9 2.3 3.4 4.2 4.2l1.8-1.3 2.6 2.2-1.4 2.4C7.4 13.5 2.5 8.7 2 3z"/></svg>
        <span>612-555-0187</span>
      </li>
      <li>
        <svg viewBox="0 0 16 16" aria-hidden="true"><path d="M1 4h14v9H1zM2 5l6 4.5L14 5v-.2H2z"/></svg>
        <span>lenapvart@orbimail.test</span>
      </li>
      <li>
        <svg viewBox="0 0 16 16" aria-hidden="true"><circle cx="8" cy="8" r="7"/></svg>
        <span>lenavartspaces.test</span>
      </li>
    </ul>
  </section>

</main>
</body>
</html>
```